Postcard 4.25"x 6" template

We need a postcard template to send information about our wellness clinic's classes and groups.
The mailing side needs space for changeable text to talk about the clinic and brief info about our classes and groups, in addition to meeting the Federal Letter Carriage Bureau requirements for address and return address area. The return address space can be fixed with our clinic's name and address on it.
The other side should be a dynamic calendar. For the time being, please use the information listed for the month of February. However, this should be changeable so that we can update the month and the events.
Somewhere on the postcard should also be a link to our website's events page:
http://www.torvesihall.com/events
Please work with our website for guidance on the look and feel of our marketing materials.
Overall it should have a natural feel.
It needs to be able to be printed at a regular printing shop and look good. It should not require a large commercial printer.
It will also need to be editable in a Word Document format.

```html
<!DOCTYPE html>
<html lang="en">
<head>
<meta charset="utf-8">
<title>Torvesi Clinic – Postcard Mailing Side</title>
<link href="https://fonts.googleapis.com/css2?family=Arimo:wght@400;700&display=swap" rel="stylesheet">
<style>
  :root {
    --paper: #ffffff;
    --leaf-green: #7ba23f;
    --leaf-soft: #cfe7d8;
    --leaf-pale: #eaf5ee;
    --ink: #555a58;
    --rule: #9bbf6a;
    --stamp-line: #6f7a5a;
  }
  * { box-sizing: border-box; margin: 0; padding: 0; }
  html, body {
    width: 1200px; height: 850px; overflow: hidden;
    background: var(--paper);
    font-family: "Arimo", Arial, sans-serif;
  }
  .postcard {
    position: relative; width: 1200px; height: 850px;
    background: var(--paper); overflow: hidden;
  }
  .backdrop-leaf {
    position: absolute; left: 560px; top: 40px;
    width: 700px; height: 840px;
    border-radius: 48% 52% 40% 60% / 55% 45% 55% 45%;
    background: radial-gradient(ellipse at 55% 45%, var(--leaf-soft) 0%, var(--leaf-pale) 60%, rgba(234,245,238,0) 100%);
  }
  .brand-leaf {
    position: absolute; left: 0; top: 0;
    width: 210px; height: 237px;
    border-radius: 50% 50% 45% 55% / 60% 60% 40% 40%;
    background: radial-gradient(ellipse at 45% 40%, var(--leaf-soft) 0%, var(--leaf-pale) 70%, rgba(234,245,238,0) 100%);
  }
  .return-address { position: absolute; left: 50px; top: 112px; }
  .brand-name {
    font-size: 42px; font-weight: 400; letter-spacing: 1px;
    color: var(--leaf-green); text-transform: uppercase; line-height: 1;
  }
  .brand-address {
    margin-top: 38px; margin-left: 173px;
    font-style: normal;
    font-size: 18px; line-height: 20px; color: var(--ink);
  }
  .message { position: absolute; left: 97px; top: 305px; width: 500px; }
  .headline {
    font-size: 28px; font-weight: 700; line-height: 28px;
    color: var(--leaf-green); text-transform: uppercase;
    letter-spacing: -0.2px;
  }
  .intro {
    margin-top: 22px; width: 490px;
    font-size: 20px; font-weight: 700; line-height: 29px; color: var(--ink);
    letter-spacing: -0.2px;
  }
  .web-link {
    position: absolute; left: 97px; top: 684px;
    font-size: 25px; font-weight: 700; color: var(--leaf-green); letter-spacing: 1px;
    text-decoration: none;
  }
  .divider {
    position: absolute; left: 650px; top: 98px; height: 697px;
    border-left: 3px dotted var(--rule);
  }
  .stamp-box {
    position: absolute; left: 957px; top: 92px;
    width: 131px; height: 123px;
    border: 2px solid var(--stamp-line);
  }
</style>
</head>
<body>
  <main class="postcard">
    <div class="backdrop-leaf" role="img" aria-label="Large faint green leaf illustration"></div>
    <div class="brand-leaf" role="img" aria-label="Green leaf illustration"></div>

    <header class="return-address">
      <div class="brand-name">Torvesi Clinic</div>
      <address class="brand-address">
        82 Alder Row<br>
        Larkfield, Westmere 40518<br>
        555) 014-2290
      </address>
    </header>

    <section class="message">
      <h1 class="headline">Holistic, naturopathic,<br>integrative mental health<br>care: we're healing minds</h1>
      <p class="intro">Welcome to the Torvesi Clinic, where true recovery from mental illness is possible. We offer hope where other therapies have failed. We guide and nurture patients through the process of change and transformation, formulate comprehensive treatment plans, help people achieve their mental health goals, and assist them in restoring balance and mental harmony.</p>
    </section>

    <a class="web-link" href="http://www.torvesihall.com/events">www.torvesihall.com/events</a>

    <div class="divider"></div>
    <div class="stamp-box"></div>
  </main>
</body>
</html>
```